Colour and Style Workshop

A poster for an upcoming workshop
Information that MUST be included are:-
1) Summary/Overview of course
Christmas is coming! Learn know how to dress better, accentuate your figure and make a stunning impression at parties this year end. Join our Colour and Style workshop conducted by renowned Designer Marcus Lheureux, a familiar name in Singapore’s fashion scene and has been a judge of Velmora Bright Makers since the competition’s first run in 2010. He is the Vice President of the Garment and Thread Council (Singapore), Chairman of its Designers and Retailers Group and Singapore’s representative to the Orient Apparel League. Lheureux also sits on the working committee that oversees KORVA rise RISE, Singapore’s fashion incubator project, which has helped launch at least 50 homegrown labels, including lio.quern and ZUE DORLO.
Course title: PLM Provide Colour and Style Coordination for Textile and Fashion Industry
Date: 16 and 23 November 2013
Time: 8.30am - 6.30pm
Venue: Maple Court, 517 Kembang Lane, #09-11, Singapore 143925
Course fees: $50 (after 90% funding from BKR for Singaporeans and SPRs)
Registration details – Serapi Junction Customer service counter, Level 2 or email us at enquiry@gowrel.org.
Shoppers who spends $20 and above in Serapi Junction will receive a $20 Lumen Arcade voucher when they register at the Customer Service Counter.
For more information about our courses and schedule, visit www.gowrel.org
Logos (some are just low res files) to include:-
• GoW.rl
• NUV (to use a place holder for now)
• BKR
• Lumen Arcade
SIZE of poster is A2.
Target Market(s)
Mostly ladies, shoppers.
20-50 years old
Industry/Entity Type
Fashion
Look and feel

```html
<!DOCTYPE html>
<html lang="en">
<head>
<meta charset="utf-8">
<title>Colour &amp; Style Workshop</title>
<link rel="stylesheet" href="https://fonts.googleapis.com/css2?family=Bodoni+Moda:wght@400;600;700&family=Lato:wght@400;700&display=swap">
<style>
  :root {
    --red: #e3101f;
    --cyan: #1aa6df;
    --navy: #2e3192;
    --purple: #662d91;
    --orange: #f26522;
    --green: #00844a;
    --grey: #5a5a5a;
    --ink: #111111;
    --text: #333333;
    --paper: #ffffff;
    --fabric-1: #f6f6f6;
    --fabric-2: #dcdcdc;
    --scene-dark: #2a2a2a;
    --scene-mid: #8a8a8a;
    --scene-light: #d8d6d4;
    --gold: #b8a27a;
    --gold-dark: #7d6c4c;
    --link: #2e3192;
  }
  * { box-sizing: border-box; margin: 0; padding: 0; }
  html, body { width: 848px; height: 1200px; overflow: hidden; background: var(--paper); }
  .poster {
    position: relative;
    width: 848px;
    height: 1200px;
    overflow: hidden;
    font-family: "Lato", sans-serif;
    color: var(--text);
    background: var(--paper);
  }
  .fabric-top {
    position: absolute; left: 0; top: 0; width: 848px; height: 300px;
    background: linear-gradient(175deg, var(--paper) 0%, var(--fabric-1) 55%, var(--fabric-2) 100%);
  }
  .boutique-scene {
    position: absolute; left: 0; top: 240px; width: 848px; height: 820px;
    background: linear-gradient(90deg, var(--scene-dark) 0%, var(--scene-mid) 40%, var(--scene-light) 70%, var(--scene-mid) 100%);
  }
  .fabric-wave {
    position: absolute; left: 0; top: 190px; width: 848px; height: 120px;
  }
  .title {
    position: absolute; left: 0; width: 848px; text-align: center;
    font-family: "Bodoni Moda", serif; line-height: 1;
    white-space: nowrap;
  }
  .title-top { top: 14px; font-size: 116px; font-weight: 400; letter-spacing: -2px; }
  .title-top .c1 { color: var(--red); }
  .title-top .c2 { color: var(--cyan); }
  .title-top .c3 { color: var(--navy); }
  .title-top .c4 { color: var(--purple); }
  .title-top .c5 { color: var(--orange); }
  .title-top .c6 { color: var(--green); }
  .title-top .style-word { color: var(--grey); }
  .title-bottom { top: 130px; font-size: 100px; font-weight: 700; color: var(--ink); }

  .info-panel {
    position: absolute; left: 38px; top: 325px; width: 428px; height: 707px;
    background: var(--paper);
    border-top-right-radius: 28px;
    padding: 22px 22px 0 28px;
  }
  .overview {
    font-size: 13.4px; line-height: 19.6px; color: var(--text);
    hyphens: auto; -webkit-hyphens: auto;
  }
  .detail { margin-top: 8px; }
  .overview + .detail { margin-top: 28px; }
  .detail-label { color: var(--red); font-size: 24px; line-height: 26px; font-weight: 400; }
  .detail-value { font-size: 14.5px; line-height: 19px; }
  .detail-value small { font-size: 11px; }
  .registration { margin-top: 22px; margin-left: -4px; font-size: 14.5px; line-height: 21px; }
  .registration .label { color: var(--red); font-size: 17px; }
  .registration a { color: var(--link); text-decoration: none; }

  .promo-frame {
    position: absolute; left: 425px; top: 655px; width: 285px; height: 180px;
    transform: rotate(-8deg);
    background: linear-gradient(135deg, #d8c9a6, var(--gold) 50%, var(--gold-dark));
    padding: 20px;
    box-shadow: 2px 4px 10px rgba(0,0,0,0.35);
  }
  .promo-inner {
    width: 100%; height: 100%;
    background: var(--paper);
    border: 3px solid #e8e2d4;
    display: flex; align-items: center; justify-content: center;
    text-align: center;
    color: var(--red); font-size: 15px; line-height: 19px;
    padding: 0 12px;
  }

  .footer {
    position: absolute; left: 0; top: 1052px; width: 848px; height: 148px;
    background: var(--paper);
  }
  .footer-note {
    position: absolute; left: 0; top: 10px; width: 848px; text-align: center;
    font-size: 19px; color: var(--text);
  }
  .footer-note a { color: var(--link); text-decoration: none; }
  .partner-row {
    position: absolute; left: 70px; top: 62px; display: flex; align-items: center; gap: 40px;
  }
  .partner {
    font-family: "Lato", sans-serif; font-weight: 700; font-size: 20px; color: var(--grey);
  }
</style>
</head>
<body>
<main class="poster">
  <div class="fabric-top"></div>
  <div class="boutique-scene" role="img" aria-label="Photo of a boutique with a clothing rail, a jewelled mannequin, a red tulle pom-pom and rows of shoes"></div>
  <svg class="fabric-wave" viewBox="0 0 848 120" preserveAspectRatio="none" aria-hidden="true">
    <path d="M0 0 H848 V60 C760 30 690 95 600 80 C520 65 470 120 380 105 C290 90 230 60 140 85 C80 100 40 110 0 100 Z" fill="#f2f2f2"/>
  </svg>

  <h1 class="title title-top"><span class="c1">C</span><span class="c2">o</span><span class="c3">l</span><span class="c4">o</span><span class="c5">u</span><span class="c6">r</span> <span class="style-word">&amp; Style</span></h1>
  <div class="title title-bottom">Workshop</div>

  <section class="info-panel">
    <p class="overview">Christmas is coming! Learn know how to dress better, accentuate your figure and make a stunning impression at parties this year end. Join our Colour and Style workshop conducted by renowned Designer Marcus Lheureux, a familiar name in Singapore’s fashion scene and has been a judge of Velmora Bright Makers since the competition’s first run in 2010. He is the Vice President of the Garment and Thread Council (Singapore), Chairman of its Designers and Retailers Group and Singapore’s representative to the Orient Apparel League. Lheureux also sits on the working committee that oversees KORVA rise RISE, Singapore’s fashion incubator project, which has helped launch at least 50 homegrown labels, including lio.quern and ZUE DORLO.</p>

    <div class="detail">
      <h2 class="detail-label">Course Title:</h2>
      <p class="detail-value">PLM Provide Colour and Style Coordination<br>for Textile and Fashion Industry</p>
    </div>
    <div class="detail">
      <h2 class="detail-label">Date:</h2>
      <p class="detail-value">16 and 23 November 2013</p>
    </div>
    <div class="detail">
      <h2 class="detail-label">Time:</h2>
      <p class="detail-value">8.30am - 6.30pm</p>
    </div>
    <div class="detail">
      <h2 class="detail-label">Venue:</h2>
      <p class="detail-value">Maple Court, 517 Kembang Lane, #09-11,<br>Singapore 143925</p>
    </div>
    <div class="detail">
      <h2 class="detail-label">Course fees:</h2>
      <p class="detail-value">$50 <small>(after 90% funding from BKR for Singaporeans and SPRs)</small></p>
    </div>

    <p class="registration"><span class="label">Registration details</span> – Serapi Junction Customer service counter, Level 2 or email us at <a href="mailto:enquiry@gowrel.org">enquiry@gowrel.org</a>.</p>
  </section>

  <aside class="promo-frame">
    <div class="promo-inner">Shoppers who spends $20 and above in Serapi Junction will receive a $20 Lumen Arcade voucher when they register at the Customer Service Counter.</div>
  </aside>

  <footer class="footer">
    <p class="footer-note">For more information about our courses and schedule, visit <a href="http://www.gowrel.org">www.gowrel.org</a></p>
    <div class="partner-row">
      <span class="partner">Lumen Arcade</span>
      <span class="partner">GoW.rl</span>
      <span class="partner">BKR</span>
      <span class="partner">NUV</span>
    </div>
  </footer>
</main>
</body>
</html>
```